Specialist Recruitment Process Outsourcing (RPO) company needs a modern, sleek website

We need a website which showcases our service offering, describes our onshore and offshore options. Our service is basically building teams of recruiters who become the outsourced (but in-house) recruiter for that specific client. Our logo colours include a light, bright green and a dark/midnight blue. This company will be targeting companies who need help with recruitment in technology, finance, engineering and other white collar industries. We are looking for a look and feeling that communicates cutting edge technology with a bright, energetic appeal. I will include some logo design files to work with.

Target Market(s)

Businesses: start ups who need to grow their staff, SMEs with regular recruitment needs, and larger businesses

Industry/Entity Type

Recruitment

Coding

Coded - Design and coding required

Number of Pages Required

4 page

Font styles to use
Sans Serif

Requirements
Must have
• Landing page should be highly visual, either with dynamic image or scrolling stills accompanies by our core service offering, values, and benefits.

A Services page will allows more detail about what we do, with a call to action.

A User Stories page will showcase some examples of how our services will help certain types of businesses.

Onshore/Offshore page will breakdown the benefits of both approaches and how combinations can work well.

Should fit the colour theming of our logo (files uploaded).

Nice to have
• Imagery can be both around business and people. We are looking for more of a "startup" feel than a corporate-y feel.

```html
<!DOCTYPE html>
<html lang="en">
<head>
<meta charset="utf-8">
<title>Crew Forge — Recruitment Teams</title>
<link href="https://fonts.googleapis.com/css2?family=Mulish:wght@400;500;600;700;800&display=swap" rel="stylesheet">
<style>
:root{
  --green:#22fa8f;
  --navy:#14105a;
  --ink:#222;
  --grey:#8a8a8a;
  --hero:#2a2a30;
  --contact:#2b2390;
  --white:#fff;
}
*{margin:0;padding:0;box-sizing:border-box}
html,body{width:1200px;height:3248px;overflow:hidden}
body{font-family:"Mulish",sans-serif;color:var(--ink);background:var(--white);position:relative}
.abs{position:absolute}
a{color:inherit;text-decoration:none}

.topline{left:0;top:0;width:1200px;height:3px;background:var(--green)}
.header{left:0;top:3px;width:1200px;height:75px;background:var(--white)}
.brand-disc{left:140px;top:-67px;width:210px;height:210px;border-radius:50%;background:var(--white);z-index:3}
.brand-name{left:140px;top:76px;width:210px;text-align:center;font-weight:700;font-size:16px;letter-spacing:4px;color:var(--ink);z-index:4}
.brand-dot{left:237px;top:36px;width:16px;height:16px;border-radius:50%;background:var(--ink);z-index:4}
.nav{top:30px;font-size:13px;font-weight:700;text-transform:uppercase;color:var(--ink)}
.nav.active{border-bottom:2px solid var(--navy);padding-bottom:4px}

.hero{left:0;top:78px;width:1200px;height:577px;background:linear-gradient(180deg,#1f1f24 0%,#2c2c33 55%,#3a3530 100%)}
.hero-title{left:0;top:160px;width:1200px;text-align:center;color:var(--white);font-size:76px;font-weight:600;letter-spacing:1px}
.hero-sub{left:0;top:260px;width:1200px;text-align:center;color:var(--white);font-size:21px;font-weight:600}
.btn{display:flex;align-items:center;justify-content:center;border-radius:24px;font-size:14px;font-weight:700;text-transform:uppercase}
.btn-green{background:var(--green);color:var(--navy)}
.btn-navy{background:var(--navy);color:var(--white)}
.hero-dot{left:1125px;width:9px;height:9px;border-radius:50%;background:var(--white)}

.section-title{left:0;width:1200px;text-align:center;font-size:42px;font-weight:600;color:var(--ink)}
.svc-h{font-size:16px;font-weight:600;color:var(--ink);text-transform:uppercase}
.svc-p{font-size:12.5px;line-height:20px;color:var(--grey);margin-top:10px}
.svc-icon{width:82px;height:82px;border-radius:50%;display:flex;align-items:center;justify-content:center}
.svc-icon.navy{background:var(--navy)}
.svc-icon.green{background:var(--green)}

.values{left:0;top:1272px;width:600px;height:492px;background:var(--green)}
.values-photo{left:600px;top:1272px;width:600px;height:492px;background:linear-gradient(160deg,#24303d 0%,#3d4650 45%,#8a6b48 80%,#d9c59e 100%)}
.values-title{left:143px;top:1338px;font-size:42px;font-weight:600;color:var(--navy)}
.values-list{left:143px;top:1418px;list-style:none}
.values-list li{display:flex;align-items:center;height:33px;font-size:17px;font-weight:500;color:var(--navy)}
.values-list svg{margin-right:18px}

.benefit-h{font-size:16px;font-weight:600;text-transform:uppercase;color:var(--ink)}

.contact{left:0;top:2455px;width:1200px;height:592px;background:linear-gradient(180deg,#2b2390,#2d2596)}
.contact-title{left:0;top:2538px;width:1200px;text-align:center;color:var(--white);font-size:42px;font-weight:600}
.field{background:var(--white);border:1px solid #ddd;font-size:13px;color:#555;padding:0 21px;display:flex;align-items:center}
.field.msg{align-items:flex-start;padding-top:20px}

.footer-nav{left:0;top:3096px;width:1200px;text-align:center;font-size:17px;font-weight:600;color:var(--ink);word-spacing:2px}
.footer-nav span{margin:0 16px}
.copy{left:0;top:3138px;width:1200px;text-align:center;font-size:14px;color:#444}
.social{top:3190px;width:24px;height:24px;border-radius:50%;background:var(--green)}
</style>
</head>
<body>

<div class="abs topline"></div>
<header class="abs header"></header>
<div class="abs brand-disc"></div>
<div class="abs brand-dot"></div>
<div class="abs brand-name">CREW FORGE</div>
<a class="abs nav active" style="left:502px">Home</a>
<a class="abs nav" style="left:577px">Services</a>
<a class="abs nav" style="left:676px">User Stories</a>
<a class="abs nav" style="left:808px">Onshore/Offshore</a>
<a class="abs nav" style="left:988px">Contact</a>

<section class="abs hero" role="img" aria-label="Photo of a smiling diverse team of six young professionals standing against a dark wall"></section>
<h1 class="abs hero-title">CREW FORGE</h1>
<p class="abs hero-sub">Lorem ipsum dolor sit amet conipiscing elit</p>
<a class="abs btn btn-green" style="left:521px;top:320px;width:157px;height:43px">Get Started</a>
<div class="abs hero-dot" style="top:176px"></div>
<div class="abs hero-dot" style="top:194px"></div>
<div class="abs hero-dot" style="top:211px"></div>
<div class="abs hero-dot" style="top:228px"></div>
<div class="abs hero-dot" style="top:245px"></div>

<h2 class="abs section-title" style="top:730px">OUR SERVICES</h2>

<div class="abs" style="left:140px;top:868px;width:248px;text-align:right">
  <div class="svc-h">Ullamco Laboris</div>
  <p class="svc-p">Lorem ipsum dolor sit aconsectetur adipiscing elit, sed do eiusmod tempor incididunt ut labore et dolore magna</p>
</div>
<div class="abs svc-icon navy" style="left:407px;top:873px">
  <svg width="30" height="38" viewBox="0 0 30 38"><path d="M3 2h16l8 8v26H3z M19 2v8h8" fill="none" stroke="#fff" stroke-width="3" stroke-linejoin="round"/></svg>
</div>
<div class="abs svc-icon green" style="left:711px;top:873px">
  <svg width="30" height="40" viewBox="0 0 30 40"><path d="M15 3a11 11 0 0 0-7 19.5c1.5 1.5 2 3 2 5h10c0-2 .5-3.5 2-5A11 11 0 0 0 15 3z" fill="none" stroke="#fff" stroke-width="3"/><rect x="10" y="30" width="10" height="3" fill="#fff"/><rect x="11" y="35" width="8" height="3" fill="#fff"/></svg>
</div>
<div class="abs" style="left:810px;top:868px;width:250px">
  <div class="svc-h">Magna Aliqua</div>
  <p class="svc-p">Lorem ipsum dolor sit aconsectetur adipiscing elit, sed do eiusmod tempor incididunt ut labore et dolore magna</p>
</div>

<div class="abs" style="left:168px;top:1084px;width:248px;text-align:right">
  <div class="svc-h">Excepteur Sin</div>
  <p class="svc-p">Lorem ipsum dolor sit aconsectetur adipiscing elit, sed do eiusmod tempor incididunt ut labore et dolore magna</p>
</div>
<div class="abs svc-icon green" style="left:434px;top:1089px">
  <svg width="48" height="40" viewBox="0 0 48 40"><rect x="18" y="2" width="12" height="10" fill="#fff"/><path d="M24 12v8M7 20h34M7 20v6M24 20v6M41 20v6" stroke="#fff" stroke-width="3" fill="none"/><rect x="1" y="27" width="12" height="11" fill="#fff"/><rect x="18" y="27" width="12" height="11" fill="#fff"/><rect x="35" y="27" width="12" height="11" fill="#fff"/></svg>
</div>
<div class="abs svc-icon navy" style="left:684px;top:1089px">
  <svg width="42" height="38" viewBox="0 0 42 38"><rect x="3" y="3" width="36" height="24" fill="none" stroke="#fff" stroke-width="4"/><rect x="18" y="27" width="6" height="6" fill="#fff"/><rect x="11" y="32" width="20" height="4" fill="#fff"/></svg>
</div>
<div class="abs" style="left:784px;top:1084px;width:250px">
  <div class="svc-h">Duis Aute Irure</div>
  <p class="svc-p">Lorem ipsum dolor sit aconsectetur adipiscing elit, sed do eiusmod tempor incididunt ut labore et dolore magna</p>
</div>

<section class="abs values"></section>
<div class="abs values-photo" role="img" aria-label="Photo of a hand holding a golden magnifying glass over a row of wooden figures with one green figure"></div>
<h2 class="abs values-title">OUR VALUES</h2>
<ul class="abs values-list">
  <li><svg width="18" height="18" viewBox="0 0 18 18"><circle cx="9" cy="9" r="8" fill="#14105a"/><path d="M5 9h7M9 5.5 12.5 9 9 12.5" stroke="#22fa8f" stroke-width="2" fill="none"/></svg>Lorem ipsum dolor sit ametconsectetur</li>
  <li><svg width="18" height="18" viewBox="0 0 18 18"><circle cx="9" cy="9" r="8" fill="#14105a"/><path d="M5 9h7M9 5.5 12.5 9 9 12.5" stroke="#22fa8f" stroke-width="2" fill="none"/></svg>Adipiscing elit, sed do eiusmod tempo</li>
  <li><svg width="18" height="18" viewBox="0 0 18 18"><circle cx="9" cy="9" r="8" fill="#14105a"/><path d="M5 9h7M9 5.5 12.5 9 9 12.5" stroke="#22fa8f" stroke-width="2" fill="none"/></svg>Incididunt ut labore et dolore magna aliqua</li>
  <li><svg width="18" height="18" viewBox="0 0 18 18"><circle cx="9" cy="9" r="8" fill="#14105a"/><path d="M5 9h7M9 5.5 12.5 9 9 12.5" stroke="#22fa8f" stroke-width="2" fill="none"/></svg>Sed ut perspiciatis unde omnis iste naerror</li>
  <li><svg width="18" height="18" viewBox="0 0 18 18"><circle cx="9" cy="9" r="8" fill="#14105a"/><path d="M5 9h7M9 5.5 12.5 9 9 12.5" stroke="#22fa8f" stroke-width="2" fill="none"/></svg>Nemo enim ipsam voluptatem</li>
  <li><svg width="18" height="18" viewBox="0 0 18 18"><circle cx="9" cy="9" r="8" fill="#14105a"/><path d="M5 9h7M9 5.5 12.5 9 9 12.5" stroke="#22fa8f" stroke-width="2" fill="none"/></svg>Neque porro quisquam estui</li>
</ul>
<a class="abs btn btn-navy" style="left:144px;top:1645px;width:142px;height:45px">Read More</a>

<h2 class="abs section-title" style="top:1854px">OUR BENEFITS</h2>

<svg class="abs" style="left:190px;top:1986px" width="120" height="120" viewBox="0 0 120 120"><rect x="20" y="20" width="80" height="80" transform="rotate(45 60 60)" fill="none" stroke="#22fa8f" stroke-width="4"/><circle cx="55" cy="55" r="12" fill="none" stroke="#14105a" stroke-width="6"/><path d="M64 64l11 11" stroke="#14105a" stroke-width="7" stroke-linecap="round"/></svg>
<div class="abs" style="left:323px;top:1998px;width:240px">
  <div class="benefit-h">Excepteur Sin</div>
  <p class="svc-p">Lorem ipsum dolor sit aconsectetur adipiscing elit, sed do eiusmod tempor incididunt ut labore et dolore magna</p>
</div>

<svg class="abs" style="left:639px;top:1986px" width="120" height="120" viewBox="0 0 120 120"><rect x="20" y="20" width="80" height="80" transform="rotate(45 60 60)" fill="none" stroke="#22fa8f" stroke-width="4"/><circle cx="60" cy="50" r="7" fill="#14105a"/><circle cx="45" cy="53" r="5" fill="#14105a"/><circle cx="75" cy="53" r="5" fill="#14105a"/><path d="M48 72c0-10 24-10 24 0z M35 70c0-8 12-9 14-5v5z M85 70c0-8-12-9-14-5v5z" fill="#14105a"/></svg>
<div class="abs" style="left:772px;top:1998px;width:240px">
  <div class="benefit-h">Voluptatem</div>
  <p class="svc-p">Lorem ipsum dolor sit aconsectetur adipiscing elit, sed do eiusmod tempor incididunt ut labore et dolore magna</p>
</div>

<svg class="abs" style="left:190px;top:2154px" width="120" height="120" viewBox="0 0 120 120"><rect x="20" y="20" width="80" height="80" transform="rotate(45 60 60)" fill="none" stroke="#22fa8f" stroke-width="4"/><g fill="#14105a"><rect x="40" y="42" width="11" height="9"/><rect x="54" y="42" width="11" height="9"/><rect x="68" y="42" width="11" height="9"/><rect x="40" y="54" width="11" height="9"/><rect x="54" y="54" width="11" height="9"/><rect x="68" y="54" width="11" height="9"/><rect x="40" y="66" width="11" height="9"/><rect x="54" y="66" width="11" height="9"/><rect x="68" y="66" width="11" height="9"/></g></svg>
<div class="abs" style="left:323px;top:2166px;width:240px">
  <div class="benefit-h">Doloremque</div>
  <p class="svc-p">Lorem ipsum dolor sit aconsectetur adipiscing elit, sed do eiusmod tempor incididunt ut labore et dolore magna</p>
</div>

<svg class="abs" style="left:639px;top:2154px" width="120" height="120" viewBox="0 0 120 120"><rect x="20" y="20" width="80" height="80" transform="rotate(45 60 60)" fill="none" stroke="#22fa8f" stroke-width="4"/><path d="M52 46v-5h16v5" fill="none" stroke="#14105a" stroke-width="4"/><rect x="40" y="46" width="40" height="28" rx="3" fill="#14105a"/><rect x="40" y="57" width="40" height="3" fill="#fff"/><rect x="56" y="55" width="8" height="7" fill="#14105a"/></svg>
<div class="abs" style="left:772px;top:2166px;width:240px">
  <div class="benefit-h">Laudantium</div>
  <p class="svc-p">Lorem ipsum dolor sit aconsectetur adipiscing elit, sed do eiusmod tempor incididunt ut labore et dolore magna</p>
</div>

<a class="abs btn btn-navy" style="left:529px;top:2328px;width:142px;height:45px">View More</a>

<section class="abs contact" role="img" aria-label="Background photo of a team of colleagues under a blue-violet tint"></section>
<h2 class="abs contact-title">CONTACT FORM</h2>
<div class="abs field" style="left:233px;top:2629px;width:360px;height:53px">First Name</div>
<div class="abs field" style="left:605px;top:2629px;width:360px;height:53px">Last Name</div>
<div class="abs field" style="left:234px;top:2694px;width:360px;height:53px">Email address</div>
<div class="abs field" style="left:606px;top:2694px;width:360px;height:53px">Phone Number</div>
<div class="abs field msg" style="left:234px;top:2759px;width:732px;height:115px">Message</div>
<a class="abs btn btn-green" style="left:529px;top:2908px;width:142px;height:44px">Submit</a>

<nav class="abs footer-nav">HOME<span>/</span>SERVICES<span>/</span>USER STORIES<span>/</span>ONSHORE/OFFSHORE<span>/</span>CONTACT</nav>
<p class="abs copy">© 2020 Crew Forge.All Rights reserved &nbsp;|&nbsp; Privacy Policy</p>
<a class="abs social" style="left:546px" aria-label="Social profile"></a>
<a class="abs social" style="left:588px" aria-label="Social profile"></a>
<a class="abs social" style="left:630px" aria-label="Social profile"></a>

</body>
</html>
```